Author/ Speaker Business Card design

I need a business card designed that will go with the branding that is already on my book and website. I like clean and straightforward, but I am not opposed to something more 'innovative'.

Target Market(s)

Colleges and Universities, educational institutions

Industry/Entity Type

Education

Contact Information for Business Card

Standard size. It should be able to be printed on good quality white or ivory paper.

Font styles to use
Sans Serif

Colors
0355a3

Requirements
Must have
• There's a blue on my website. It should have some blue. My logo is at the top. It should have the logo incorporated somewhere on it. My name, Author | Speaker | Teacher | Trainer, my phone number (+31 64-207 5819), my email address (milo@theboldlearner.example), Social media icons (twitter, Instagram, LinkedIn) with the addresses (twitter @writermilofenwick, Instagram - theboldlearner, LinkedIn - theboldlearner) By they way, the website is www.theboldlearner.example. There is a photo of the book on the website. Also, my full name is Milo Fenwick
Nice to have
• Try to use the font that is on the website and book. Also, if you could get that blue, that would be great.
Should not have
• My photo

```html
<!DOCTYPE html>
<html lang="en">
<head>
<meta charset="utf-8">
<title>Milo Fenwick – Business Card</title>
<link rel="stylesheet" href="https://fonts.googleapis.com/css2?family=Montserrat:wght@400;500;700&display=swap">
<style>
  :root {
    --brand-blue: #0355a3;
    --paper: #ffffff;
    --ink: #222222;
    --backdrop: #8c8c8c;
  }
  * { box-sizing: border-box; margin: 0; padding: 0; }
  html, body {
    width: 1200px; height: 1200px; overflow: hidden;
    background: var(--backdrop);
    font-family: "Montserrat", Arial, sans-serif;
  }
  .card {
    position: absolute;
    top: 435px;
    width: 540px; height: 330px;
    overflow: hidden;
  }
  .card--front { left: 40px; background: var(--paper); }
  .card--back { left: 620px; background: var(--brand-blue); }

  .brand-name {
    position: absolute;
    display: flex; align-items: center; gap: 10px;
    font-weight: 700; letter-spacing: 0.2px;
  }
  .brand-name__dot {
    width: 14px; height: 14px; border-radius: 50%;
  }
  .card--front .brand-name { right: 22px; top: 30px; font-size: 26px; color: var(--brand-blue); }
  .card--front .brand-name__dot { background: var(--brand-blue); }
  .card--back .brand-name { left: 0; right: 0; top: 142px; justify-content: center; font-size: 30px; color: var(--paper); }
  .card--back .brand-name__dot { background: var(--paper); }

  .holder-name {
    position: absolute; left: 24px; top: 84px;
    font-size: 23px; color: var(--brand-blue); font-weight: 400; letter-spacing: 0.5px;
  }
  .holder-name strong { font-weight: 700; }
  .rule { position: absolute; left: 0; width: 252px; background: var(--brand-blue); }
  .rule--upper { top: 113px; height: 2px; }
  .rule--lower { top: 132px; height: 1px; }
  .holder-roles {
    position: absolute; left: 24px; top: 117px;
    font-size: 9.5px; color: var(--ink); letter-spacing: 0.3px;
  }

  .contact-list {
    position: absolute; right: 22px; top: 132px;
    list-style: none;
    display: flex; flex-direction: column; align-items: flex-end; gap: 11px;
  }
  .contact-list li {
    display: flex; align-items: center; gap: 10px;
    font-size: 13.5px; color: var(--ink);
  }
  .contact-icon { width: 20px; height: 20px; }

  .band-rule {
    position: absolute; left: 0; right: 0; top: 228px; height: 3px; background: var(--brand-blue);
  }
  .social-band {
    position: absolute; left: 0; right: 0; top: 236px; bottom: 0;
    background: var(--brand-blue);
    display: grid; grid-template-columns: repeat(3, 1fr);
    padding: 0 10px;
  }
  .social-item {
    display: flex; flex-direction: column; align-items: center;
    padding-top: 20px; gap: 12px;
    color: var(--paper); font-size: 12px;
  }
  .social-mark { width: 16px; height: 16px; border-radius: 3px; background: var(--paper); }

  .back-url {
    position: absolute; left: 0; right: 0; top: 280px;
    text-align: center; color: var(--paper); font-size: 14px; font-weight: 500;
  }
</style>
</head>
<body>
  <section class="card card--front" aria-label="Business card front">
    <div class="brand-name"><span class="brand-name__dot"></span>The Bold Learner</div>

    <h1 class="holder-name"><strong>MILO</strong> FENWICK</h1>
    <div class="rule rule--upper"></div>
    <p class="holder-roles">AUTHOR | SPEAKER | TEACHER | TRAINER</p>
    <div class="rule rule--lower"></div>

    <ul class="contact-list">
      <li>+31 64-207 5819
        <svg class="contact-icon" viewBox="0 0 20 20" aria-hidden="true">
          <circle cx="10" cy="10" r="10" fill="#0355a3"/>
          <rect x="7" y="4.5" width="6" height="11" rx="1.2" fill="none" stroke="#fff" stroke-width="1.3"/>
          <circle cx="10" cy="13.3" r="0.8" fill="#fff"/>
        </svg>
      </li>
      <li>milo@theboldlearner.example
        <svg class="contact-icon" viewBox="0 0 20 20" aria-hidden="true">
          <circle cx="10" cy="10" r="10" fill="#0355a3"/>
          <rect x="5" y="6.5" width="10" height="7" fill="none" stroke="#fff" stroke-width="1.2"/>
          <path d="M5 6.5 L10 10.8 L15 6.5" fill="none" stroke="#fff" stroke-width="1.2"/>
        </svg>
      </li>
      <li>www.theboldlearner.example
        <svg class="contact-icon" viewBox="0 0 20 20" aria-hidden="true">
          <circle cx="10" cy="10" r="10" fill="#0355a3"/>
          <circle cx="10" cy="10" r="5" fill="none" stroke="#fff" stroke-width="1.2"/>
          <ellipse cx="10" cy="10" rx="2.2" ry="5" fill="none" stroke="#fff" stroke-width="1"/>
          <line x1="5" y1="10" x2="15" y2="10" stroke="#fff" stroke-width="1"/>
        </svg>
      </li>
    </ul>

    <div class="band-rule"></div>
    <div class="social-band">
      <div class="social-item"><span class="social-mark"></span>@writermilofenwick</div>
      <div class="social-item"><span class="social-mark"></span>theboldlearner</div>
      <div class="social-item"><span class="social-mark"></span>theboldlearner</div>
    </div>
  </section>

  <section class="card card--back" aria-label="Business card back">
    <div class="brand-name"><span class="brand-name__dot"></span>The Bold Learner</div>
    <p class="back-url">www.theboldlearner.example</p>
  </section>
</body>
</html>
```